Redesign of Business Cards to Update them!

We want a full overhaul of our business cards! We have a design that is almost 5 years old and it needs to be updated to be current

Address is 437 Dunmore Lane Suite C San Bernardino CA 92408
PH: 9094718263
Zorlivo.com

Hours M-F 10AM-4PM
Sat and Sunday Closed

```html
<!DOCTYPE html>
<html lang="en">
<head>
<meta charset="utf-8">
<title>Zorlivo Business Card</title>
<link rel="stylesheet" href="https://fonts.googleapis.com/css2?family=Roboto+Condensed:wght@700&family=Roboto:wght@400;700&display=swap">
<style>
  :root {
    --backdrop: #d1d2d4;
    --paper: #ffffff;
    --ink: #0a0a0b;
    --accent: #ed1c24;
  }
  * { margin: 0; padding: 0; box-sizing: border-box; }
  html, body { width: 962px; height: 1200px; overflow: hidden; }
  body { background: var(--backdrop); position: relative; font-family: "Roboto", Arial, sans-serif; }

  .card { position: absolute; left: 30px; width: 905px; height: 543px; background: var(--paper); overflow: hidden; }
  .card--front { top: 40px; }
  .card--back { top: 617px; }

  .front-graphics { position: absolute; inset: 0; }

  .hours { position: absolute; left: 0; right: 0; top: 88px; text-align: center;
    font-family: "Roboto Condensed", "Arial Narrow", sans-serif; font-weight: 700; line-height: 1; }
  .hours__open { color: var(--accent); font-size: 72px; letter-spacing: 0.5px; }
  .hours__closed { color: var(--ink); font-size: 72px; margin-top: 6px; }

  .divider { position: absolute; left: 103px; top: 242px; width: 695px; height: 14px; }

  .address { position: absolute; left: 0; right: 0; top: 270px; text-align: center;
    font-size: 32px; line-height: 40px; color: var(--ink); letter-spacing: 0.3px; padding-right: 10px; }

  .contact-pill { position: absolute; left: 117px; top: 368px; width: 658px; height: 96px;
    background: var(--paper); border: 3px solid var(--ink); border-radius: 46px;
    display: flex; align-items: center; padding-left: 44px; gap: 34px; font-size: 35px; color: var(--ink); }
  .contact-item { display: flex; align-items: center; gap: 12px; }
  .contact-item svg { width: 36px; height: 36px; flex: none; }

  .mascot-art { position: absolute; left: 187px; top: 101px; width: 487px; height: 212px;
    background: linear-gradient(90deg, #f3c4c6, #ed1c24 50%, #f3c4c6); border-radius: 12px; }

  .brand-name { position: absolute; left: 0; right: 0; top: 350px; text-align: center;
    font-family: "Roboto", Arial, sans-serif; font-weight: 700; font-size: 84px; color: var(--ink); letter-spacing: 2px; }
</style>
</head>
<body>

<section class="card card--front">
  <svg class="front-graphics" viewBox="0 0 905 543" width="905" height="543">
    <rect class="base-band" x="0" y="421" width="905" height="122" fill="var(--ink)"/>
    <polygon class="accent-stripe" points="905,181 905,229 661,543 621,543" fill="var(--accent)"/>
    <polygon class="accent-stripe" points="905,261 905,286 703,543 684,543" fill="var(--accent)"/>
  </svg>

  <div class="hours">
    <div class="hours__open">HOURS M-F 10AM-4PM</div>
    <div class="hours__closed">SAT AND SUNDAY CLOSED</div>
  </div>

  <svg class="divider" viewBox="0 0 695 14">
    <line x1="0" y1="7" x2="330" y2="7" stroke="var(--ink)" stroke-width="2.5" stroke-dasharray="8 7"/>
    <polygon points="334,7 347,1 360,7 347,13" fill="var(--ink)"/>
    <line x1="366" y1="7" x2="695" y2="7" stroke="var(--ink)" stroke-width="2.5" stroke-dasharray="8 7"/>
  </svg>

  <p class="address">437 Dunmore Lane Suite C, San Bernardino<br>CA 92408</p>

  <div class="contact-pill">
    <div class="contact-item">
      <svg viewBox="0 0 36 36" aria-hidden="true">
        <path d="M3 13 C3 5 33 5 33 13 L33 16 L25 16 L25 11 L11 11 L11 16 L3 16 Z" fill="var(--accent)"/>
        <path d="M12 14 L24 14 L31 24 L31 32 L5 32 L5 24 Z" fill="var(--accent)"/>
        <circle cx="18" cy="23" r="4.5" fill="var(--paper)"/>
      </svg>
      <span>9094718263</span>
    </div>
    <div class="contact-item">
      <svg viewBox="0 0 36 36" aria-hidden="true" fill="none" stroke="var(--accent)" stroke-width="2.5">
        <circle cx="18" cy="18" r="15"/>
        <ellipse cx="18" cy="18" rx="7" ry="15"/>
        <line x1="18" y1="3" x2="18" y2="33"/>
        <line x1="3" y1="18" x2="33" y2="18"/>
        <path d="M6 10 H30 M6 26 H30"/>
      </svg>
      <span>Zorlivo.com</span>
    </div>
  </div>
</section>

<section class="card card--back">
  <div class="mascot-art" role="img" aria-label="Illustration of two red cartoon mascots joined by an arrow, one holding a broken phone and one holding a repaired phone"></div>
  <div class="brand-name">Zorlivo</div>
</section>

</body>
</html>
```